Dr. Lumora needs a design for its website!

*Only need the design, coding is not required.
*Need desktop version ($500) and mobile/tablet version ($200)
*The attached files are not the exact layout we want, they are just for you to know what information should be included in those pages.
*The function of our website is like www.qavlo.hk
*For the background picture, prefer a lively picture and chinese people in it, NOT necessarily need a doctor or sick person in the picture

***Don't just copy the layout from the attachments or from the reference website, we are looking for creative ideas, non-ordinary designs!!!****

We are developing a website for the public to search a doctor by different criteria. At the initial stage, we need 4 pages to start with and other pages at later stage. I have attached the general idea of these pages but not necessarily to be exactly the same, I am looking for some new ideas.

This website needs a professional, modern, simple and user friendly design. The main color to be used in the website will be same as the color (R:0 G:139 B:205) used in our logo (see attached). We don't have any particular thoughts for the other color and the font to be used in the website. Can try to use circle outline for the icon in the navigation bar.

1. Home: will include 4 sections (see attached)

2. Doctor's details (see attached)

3. Health information: will include a short descriptions of this Health Info page and 5 sections (see attached)

4. News (see attached)

Reason: Not too many suitable designs to choose from and need more time to go through the designs

All

Medical

4 page

• must not be same as or looks too much like www.qavlo.hk
• prefer not to use black and red color

```html
<!DOCTYPE html>
<html lang="en">
<head>
<meta charset="utf-8">
<title>Dr. Lumora – Find a Doctor</title>
<link rel="stylesheet" href="https://fonts.googleapis.com/css2?family=Open+Sans:wght@400;600;700&display=swap">
<style>
:root{
  --brand:#008bcd;
  --brand-dark:#0a6fa6;
  --navy:#0d2a45;
  --navy-deep:#081d31;
  --ink:#333;
  --muted:#777;
  --line:#d8dde2;
  --panel:rgba(255,255,255,.93);
  --row-alt:#eef4f8;
  --pink:#e0529a;
}
*{box-sizing:border-box;margin:0;padding:0}
html,body{width:809px;height:1200px;overflow:hidden}
body{font-family:"Open Sans",Arial,sans-serif;color:var(--ink);background:#fff;position:relative;font-size:11px}

.site-header{position:absolute;top:0;left:0;width:809px;height:97px;background:#fff}
.brand{position:absolute;left:25px;top:24px;display:flex;align-items:center;gap:10px}
.brand-dot{width:44px;height:44px;border-radius:50%;background:var(--brand)}
.brand-name{font-size:30px;font-weight:700;color:var(--brand);letter-spacing:-.5px}
.top-ribbon{position:absolute;right:0;top:0;width:330px;height:36px;background:var(--navy);
  clip-path:polygon(18px 0,100% 0,100% 100%,0 100%);display:flex;align-items:center;justify-content:flex-end;gap:22px;padding-right:25px;color:#fff;font-size:11px}
.top-ribbon span{display:flex;align-items:center;gap:6px}
.lang{position:absolute;right:25px;top:50px;font-size:10px;color:var(--brand)}

.main-nav{position:absolute;top:97px;left:0;width:809px;height:28px;background:var(--brand);display:flex;align-items:center;padding-left:25px}
.main-nav a{color:#fff;text-decoration:none;font-size:11px;font-weight:600;height:28px;line-height:28px;padding:0 18px}
.main-nav a.active{background:var(--navy)}
.nav-search{margin-left:auto;margin-right:25px;width:190px;height:20px;background:#fff;display:flex;align-items:center;gap:6px;padding-left:7px;font-size:10px;color:var(--muted);font-weight:600}

.hero{position:absolute;top:125px;left:0;width:809px;height:555px;
  background:linear-gradient(135deg,#7c93a8 0%,#a6b7c4 30%,#c9b8a4 55%,#8aa2b6 80%,#6d8499 100%)}
.hero-veil{position:absolute;inset:0;background:rgba(235,242,248,.35)}

.panel{position:absolute;left:40px;width:330px;background:var(--panel);border-top:3px solid var(--brand);padding:14px 18px}
.panel h2{text-align:center;font-size:14px;font-weight:700;color:var(--ink);margin-bottom:14px}
.field{display:flex;align-items:center;margin-bottom:9px;font-size:10px}
.field label{width:88px;flex:none}
.input{flex:1;height:20px;border:1px solid var(--line);background:#fff;position:relative}
.input.select::after{content:"";position:absolute;right:7px;top:5px;width:6px;height:6px;border-right:2px solid var(--navy);border-bottom:2px solid var(--navy);transform:rotate(45deg)}
.radio{display:flex;gap:18px;align-items:center}
.radio span{display:flex;align-items:center;gap:5px}
.radio i{width:10px;height:10px;border:1px solid #999;border-radius:50%;background:#fff;display:inline-block}
.btn{display:inline-block;height:22px;line-height:22px;padding:0 20px;font-size:10px;font-weight:700;color:#fff;background:var(--brand)}
.btn.dark{background:var(--navy)}
.login{top:25px;height:190px}
.login .actions{display:flex;align-items:center;gap:14px;margin-left:88px;margin-top:4px;font-size:10px}
.finder{top:227px;height:308px}
.finder .actions{display:flex;justify-content:center;gap:8px;margin-top:12px}

.perks{position:absolute;left:430px;top:40px;width:350px}
.perks h2{display:flex;align-items:center;gap:10px;font-size:15px;font-weight:700;color:var(--navy);margin-bottom:28px}
.perk{display:flex;align-items:center;gap:14px;margin-bottom:24px;font-size:11px;font-weight:600;color:var(--ink)}
.perk-icon{width:54px;height:54px;border-radius:50%;background:var(--brand);border:3px solid #fff;box-shadow:0 0 0 2px var(--brand);display:flex;align-items:center;justify-content:center;flex:none}
.perk-text{background:rgba(255,255,255,.85);padding:7px 14px;flex:1}

.results{position:absolute;top:680px;left:0;width:809px;height:278px;background:#fff}
.results h2{display:flex;align-items:center;justify-content:center;gap:8px;font-size:16px;font-weight:700;color:var(--navy);margin-top:14px}
.results-table{position:absolute;left:25px;top:55px;width:759px;border-collapse:collapse;font-size:10px}
.results-table th{background:var(--brand);color:#fff;font-weight:600;height:22px}
.results-table td{height:31px;text-align:center;border-bottom:1px solid #e4e8ec}
.results-table td:first-child{text-align:left;padding-left:14px}
.results-table tr:nth-child(even) td{background:var(--row-alt)}

.site-footer{position:absolute;top:958px;left:0;width:809px;height:207px;background:var(--navy)}
.footer-brand{position:absolute;left:25px;top:22px;display:flex;align-items:center;gap:8px}
.footer-brand .brand-dot{width:36px;height:36px}
.footer-brand .brand-name{font-size:24px;color:#fff}
.footer-about{position:absolute;left:280px;top:20px;width:190px;color:#b9c7d4}
.site-footer h3{font-size:11px;font-weight:700;color:#fff;margin-bottom:10px}
.footer-about p{font-size:9px;line-height:1.6}
.footer-contact{position:absolute;left:555px;top:20px;width:229px}
.footer-contact .input{display:block;height:18px;margin-bottom:6px;background:#e9eef2;border:none;font-size:9px;color:var(--muted);padding:3px 6px}
.footer-contact .input.msg{height:52px}
.footer-contact .btn{float:right;height:20px;line-height:20px;background:var(--navy-deep);border:1px solid #41607d;font-size:9px}
.copyright{position:absolute;top:1165px;left:0;width:809px;height:35px;background:var(--brand);color:#fff;font-size:9px;display:flex;align-items:center;padding:0 25px}
.social{margin-left:auto;display:flex;gap:6px}
.social i{width:16px;height:16px;border-radius:50%;background:#fff;display:block}
</style>
</head>
<body>

<header class="site-header">
  <div class="brand"><span class="brand-dot"></span><span class="brand-name">Dr. Lumora</span></div>
  <div class="top-ribbon">
    <span><svg width="11" height="11" viewBox="0 0 24 24"><path fill="#fff" d="M6.6 10.8a15 15 0 0 0 6.6 6.6l2.2-2.2c.3-.3.7-.4 1-.2 1.1.4 2.3.6 3.6.6.6 0 1 .4 1 1V20c0 .6-.4 1-1 1A17 17 0 0 1 3 4c0-.6.4-1 1-1h3.5c.6 0 1 .4 1 1 0 1.3.2 2.5.6 3.6.1.3 0 .7-.2 1z"/></svg>+852-260-48-19</span>
    <span><svg width="12" height="10" viewBox="0 0 24 18"><rect x="1" y="1" width="22" height="16" fill="none" stroke="#fff" stroke-width="2"/><path d="M1 1l11 9 11-9" fill="none" stroke="#fff" stroke-width="2"/></svg>hello@lumora-care.hk</span>
  </div>
  <div class="lang">ENGLISH | 繁體中文 | 简体</div>
</header>

<nav class="main-nav">
  <a class="active">HOME</a><a>HEALTH INFO</a><a>NEWS</a><a>ABOUT US</a><a>CONTACT US</a>
  <div class="nav-search"><svg width="10" height="10" viewBox="0 0 24 24"><circle cx="10" cy="10" r="7" fill="none" stroke="#008bcd" stroke-width="3"/><path d="M15 15l7 7" stroke="#008bcd" stroke-width="3"/></svg>SEARCH</div>
</nav>

<section class="hero">
  <div role="img" aria-label="Lively photo of a busy Hong Kong street crowd" class="hero-veil"></div>

  <form class="panel login">
    <h2>Member Login</h2>
    <div class="field"><label>Login Email :</label><span class="input"></span></div>
    <div class="field"><label>Password :</label><span class="input"></span></div>
    <div class="actions"><span class="btn">LOGIN</span><span>Forget Password</span></div>
  </form>

  <form class="panel finder">
    <h2>Find a Doctor</h2>
    <div class="field"><label>Doctor's Name :</label><span class="input"></span></div>
    <div class="field"><label>Gender :</label><span class="radio"><span><i></i>Male</span><span><i></i>Female</span></span></div>
    <div class="field"><label>Specialism :</label><span class="input select"></span></div>
    <div class="field"><label>Symptom :</label><span class="input select"></span></div>
    <div class="field"><label>District :</label><span class="input select"></span></div>
    <div class="field"><label>Phone Number :</label><span class="input"></span></div>
    <div class="actions"><span class="btn">SEARCH</span><span class="btn dark">RESET</span></div>
  </form>

  <div class="perks">
    <h2><svg width="26" height="26" viewBox="0 0 24 24"><circle cx="12" cy="12" r="11" fill="#008bcd"/><path d="M12 6v12M6 12h12" stroke="#fff" stroke-width="3"/></svg>BECOME A DR. LUMORA MEMBER</h2>
    <div class="perk"><span class="perk-icon"><svg width="24" height="24" viewBox="0 0 24 24" fill="none" stroke="#fff" stroke-width="2"><rect x="3" y="4" width="18" height="16"/><path d="M7 9h10M7 13h10M7 17h6"/></svg></span><span class="perk-text">First-Hand Health News</span></div>
    <div class="perk"><span class="perk-icon"><svg width="24" height="24" viewBox="0 0 24 24" fill="none" stroke="#fff" stroke-width="2"><path d="M3 12V3h9l9 9-9 9z"/><circle cx="8" cy="8" r="1.5"/></svg></span><span class="perk-text">Exclusive Promotions</span></div>
    <div class="perk"><span class="perk-icon"><svg width="24" height="24" viewBox="0 0 24 24" fill="none" stroke="#fff" stroke-width="2"><path d="M3 4h18v12H9l-5 4V4z"/><path d="M8 10h8"/></svg></span><span class="perk-text">Instant Health Advices</span></div>
    <div class="perk"><span class="perk-icon"><svg width="24" height="24" viewBox="0 0 24 24" fill="none" stroke="#fff" stroke-width="2"><rect x="4" y="3" width="16" height="18" rx="2"/><path d="M12 8v8M8 12h8"/></svg></span><span class="perk-text">Free Health Seminars / Talks</span></div>
    <div class="perk"><span class="perk-icon"><svg width="24" height="24" viewBox="0 0 24 24" fill="none" stroke="#fff" stroke-width="2"><rect x="3" y="5" width="18" height="16"/><path d="M3 10h18M8 3v4M16 3v4"/><path d="M9 15l2 2 4-4"/></svg></span><span class="perk-text">Priority Doctor Appointments</span></div>
  </div>
</section>

<section class="results">
  <h2><svg width="20" height="20" viewBox="0 0 24 24"><circle cx="10" cy="10" r="7" fill="none" stroke="#008bcd" stroke-width="3"/><path d="M15 15l7 7" stroke="#008bcd" stroke-width="3"/></svg>SEARCH RESULTS</h2>
  <table class="results-table">
    <thead><tr><th>Name</th><th>Gender</th><th>Specialism</th><th>Hospital</th><th>Address</th><th>District</th><th>Phone</th></tr></thead>
    <tbody>
      <tr><td>Lam Oscar</td><td><svg width="12" height="14" viewBox="0 0 12 14"><circle cx="6" cy="4" r="3.5" fill="#008bcd"/><path d="M0 14c0-4 2.5-6 6-6s6 2 6 6z" fill="#008bcd"/></svg></td><td>Cardiology</td><td>Private</td><td>18 Cedar Lane</td><td>Kwun Tong</td><td>2731-4058</td></tr>
      <tr><td>Tse Mei Ling, Joan</td><td><svg width="12" height="14" viewBox="0 0 12 14"><circle cx="6" cy="4" r="3.5" fill="#e0529a"/><path d="M0 14c0-4 2.5-6 6-6s6 2 6 6z" fill="#e0529a"/></svg></td><td>Dentistry</td><td>Private</td><td>52 Harbour St</td><td>Kowloon</td><td>2846-1937</td></tr>
      <tr><td>Wong K T Adrian</td><td><svg width="12" height="14" viewBox="0 0 12 14"><circle cx="6" cy="4" r="3.5" fill="#008bcd"/><path d="M0 14c0-4 2.5-6 6-6s6 2 6 6z" fill="#008bcd"/></svg></td><td>Endocrinology</td><td>Private</td><td>7 Maple Road</td><td>Sai Kung</td><td>2958-6204</td></tr>
      <tr><td>Ho Chun, Marcus</td><td><svg width="12" height="14" viewBox="0 0 12 14"><circle cx="6" cy="4" r="3.5" fill="#008bcd"/><path d="M0 14c0-4 2.5-6 6-6s6 2 6 6z" fill="#008bcd"/></svg></td><td>Gastroenterology</td><td>Private</td><td>31 Orchid Path</td><td>Tai Po</td><td>2615-7392</td></tr>
      <tr><td>Yip Siu Wah</td><td><svg width="12" height="14" viewBox="0 0 12 14"><circle cx="6" cy="4" r="3.5" fill="#e0529a"/><path d="M0 14c0-4 2.5-6 6-6s6 2 6 6z" fill="#e0529a"/></svg></td><td>General Surgery</td><td>Private</td><td>96 Willow Ave</td><td>Wan Chai</td><td>2537-8841</td></tr>
    </tbody>
  </table>
</section>

<footer class="site-footer">
  <div class="footer-brand"><span class="brand-dot"></span><span class="brand-name">Dr. Lumora</span></div>
  <div class="footer-about">
    <h3>ABOUT DR LUMORA</h3>
    <p>Dr. Lumora helps people in Hong Kong find the right doctor quickly. Search by name, specialism, symptom or district, compare clinics and hospitals, and book an appointment with confidence. Members also receive health news, advice and exclusive offers from our trusted medical partners.</p>
  </div>
  <form class="footer-contact">
    <h3>CONTACT US</h3>
    <span class="input">Name</span>
    <span class="input">Email</span>
    <span class="input msg">Message</span>
    <span class="btn">SUBMIT</span>
  </form>
</footer>

<div class="copyright">COPYRIGHT © 2016 DR LUMORA. ALL RIGHTS RESERVED.
  <div class="social"><i></i><i></i><i></i></div>
</div>

</body>
</html>
```